Veltra Homes Real Estate Brokerage Recruiting Flyer

We are a real estate brokerage looking to hire more real estate agents. We need to list everything we have to offer as a company so real estate agents will join our company. this is our company website: www.Veltrahomes.example .

100% COMMISSION NO MONTHLY FEE
$450 Flat Transaction FEE

What We Offer:
24/7 Office Access
Free E & O Insurance for 1st Year
Free Online CE and PLE
Free 1,000 Business Cards
Free Professional Social Media Marketing
Free Printing, Scanning, and Copies
Free Buyer and Seller Presentation Packages
Free Papervane Cloud Based Document Management Access
Access to our Internal Brokerage Forum
Company Profit Sharing!
Private Offices Available to Rent

*Lead Generation Software with over 3,000 Leads
*10 Leads to Start
* Free Personal CRM and Website
*Restrictions and Rules apply

Company Address:
4817 Marlow Creek Road
Suite 412
Fairfax, VA 22147
Phone: 703-241-7086
email: info@veltrahomes.example

Target Market(s)

Real Estate Agents

Industry/Entity Type

Real Estate

Colors
0555a3
ffffff

Requirements
Must have
• 100% COMMISSION NO MONTHLY FEE
$450 Flat Transaction FEE

What We Offer:
24/7 Office Access
Free Online CE and PLE
Free 1,000 Business Cards
Company Profit Sharing!

*10 Leads to Start

Company Address:
4817 Marlow Creek Road
Suite 412
Fairfax, VA 22147
Phone: 703-241-7086

```html
<!DOCTYPE html>
<html lang="en">
<head>
<meta charset="utf-8">
<title>Veltra Homes – Agent Recruiting Flyer</title>
<link href="https://fonts.googleapis.com/css2?family=Josefin+Sans:wght@400;600;700&family=Roboto+Condensed:wght@400;700&display=swap" rel="stylesheet">
<style>
  :root{
    --navy:#273b7b;
    --navy-deep:#1f2f66;
    --white:#ffffff;
    --ink:#1d1d1f;
    --footer:#d6d7d9;
    --shadow:#c9cacd;
    --photo-a:#2b3f80;
    --photo-b:#8fa6c8;
    --photo-c:#dfe6ee;
  }
  *{box-sizing:border-box;margin:0;padding:0}
  html,body{width:928px;height:1200px;overflow:hidden;background:var(--white)}
  .flyer{position:relative;width:928px;height:1200px;overflow:hidden;background:var(--white);font-family:"Josefin Sans",sans-serif;color:var(--ink)}

  .brand{position:absolute;top:0;left:0;width:928px;height:144px;display:flex;align-items:center;justify-content:center;gap:14px}
  .brand-mark{width:34px;height:34px;background:var(--navy)}
  .brand-name{font-family:"Josefin Sans",sans-serif;font-weight:400;font-size:40px;letter-spacing:2px;color:var(--navy);padding-top:6px}

  .hero{position:absolute;top:144px;left:0;width:928px;height:388px;background:var(--navy)}
  .hero-photo{position:absolute;top:0;right:0;width:492px;height:388px;
    background:linear-gradient(100deg,var(--navy) 0%,var(--photo-a) 10%,var(--photo-b) 55%,var(--photo-c) 100%)}
  .notch{position:absolute;width:0;height:0;border-left:14px solid transparent;border-right:14px solid transparent}
  .notch-top{top:144px;left:445px;border-top:14px solid var(--white)}
  .notch-bottom{top:532px;left:445px;border-top:14px solid var(--navy)}

  .offer-headline{position:absolute;left:32px;top:116px;color:var(--white);white-space:nowrap}
  .headline-light{font-weight:400;font-size:36px;letter-spacing:0.4px;line-height:40px;display:block}
  .headline-bold{font-weight:700;font-size:36px;letter-spacing:0.6px;line-height:42px;display:block}
  .fee-box{position:absolute;left:31px;top:201px;width:348px;height:29px;background:var(--white);color:var(--navy);
    font-weight:600;font-size:20px;letter-spacing:2.6px;line-height:32px;padding-left:10px;white-space:nowrap}

  .section-title{position:absolute;left:347px;top:582px;width:224px;height:37px;background:var(--navy);color:var(--white);
    font-weight:400;font-size:26px;text-align:center;line-height:41px;box-shadow:0 4px 0 var(--shadow)}

  .benefits{position:absolute;top:650px;list-style:none;font-family:"Roboto Condensed",sans-serif;font-size:19.5px;color:var(--ink);white-space:nowrap}
  .benefits-left{left:26px}
  .benefits-right{left:523px}
  .benefits li{position:relative;padding-left:34px;line-height:33.3px}
  .benefits li svg{position:absolute;left:0;top:9px;width:17px;height:17px}
  .benefits .continued{padding-left:34px}

  .perks{position:absolute;top:876px;left:0;width:928px;height:228px;background:linear-gradient(180deg,var(--navy) 0%,var(--navy-deep) 100%)}
  .notch-perks{position:absolute;top:0;left:445px;width:0;height:0;border-left:14px solid transparent;border-right:14px solid transparent;border-top:14px solid var(--white)}
  .perk{position:absolute;top:30px;text-align:center;color:var(--white);font-size:20px;line-height:24px}
  .perk svg{display:block;margin:0 auto 18px;width:76px;height:76px}
  .perk-1{left:0;width:232px}
  .perk-2{left:249px;width:208px}
  .perk-3{left:459px;width:232px}
  .perk-4{left:712px;width:216px}
  .divider{position:absolute;top:50px;height:86px;border-left:1px dashed rgba(255,255,255,.45)}

  .contact{position:absolute;top:1104px;left:0;width:928px;height:96px;background:var(--footer)}
  .address-tab{position:absolute;top:1085px;left:356px;width:215px;height:44px}
  .address-tab span{position:absolute;inset:0;text-align:center;line-height:50px;font-size:26px;color:var(--navy)}
  .contact-line{position:absolute;top:1150px;left:20px;right:20px;display:flex;align-items:center;justify-content:center;
    font-family:"Roboto Condensed",sans-serif;font-weight:700;color:var(--navy);white-space:nowrap}
  .contact-item{display:flex;align-items:center;gap:8px;font-size:16px;flex-shrink:0;white-space:nowrap}
  .contact-item svg{width:15px;height:18px;flex-shrink:0}
  .contact-phone{font-size:22px}
  .sep{margin:0 18px;font-weight:400;font-size:18px;flex-shrink:0}
</style>
</head>
<body>
<div class="flyer">

  <header class="brand">
    <span class="brand-mark"></span>
    <span class="brand-name">Veltra Homes</span>
  </header>

  <section class="hero">
    <div class="hero-photo" role="img" aria-label="Photo of a smiling real estate agent in a suit meeting a client at an office desk"></div>
    <div class="offer-headline">
      <span class="headline-light">100% COMMISSION</span>
      <span class="headline-bold">NO MONTHLY FEE</span>
    </div>
    <div class="fee-box">$450 Flat Transaction Fee</div>
  </section>
  <div class="notch notch-top"></div>
  <div class="notch notch-bottom"></div>

  <h2 class="section-title">What We Offer</h2>

  <svg width="0" height="0" style="position:absolute">
    <defs>
      <symbol id="tick" viewBox="0 0 17 17">
        <path d="M13 8.5V15H2V3h9" fill="none" stroke="#273b7b" stroke-width="2"/>
        <path d="M5 8l3 3 7-8" fill="none" stroke="#273b7b" stroke-width="2"/>
      </symbol>
    </defs>
  </svg>

  <ul class="benefits benefits-left">
    <li><svg><use href="#tick"/></svg>24/7 Office Access</li>
    <li><svg><use href="#tick"/></svg>Free E &amp; O Insurance for 1st Year</li>
    <li><svg><use href="#tick"/></svg>Free Online CE and PLE</li>
    <li><svg><use href="#tick"/></svg>Free 1,000 Business Cards</li>
    <li><svg><use href="#tick"/></svg>Free Professional Social Media Marketing</li>
    <li><svg><use href="#tick"/></svg>Free Printing, Scanning, and Copies</li>
  </ul>
  <ul class="benefits benefits-right">
    <li><svg><use href="#tick"/></svg>Free Buyer and Seller Presentation Packages</li>
    <li><svg><use href="#tick"/></svg>Free Papervane Cloud Based Document</li>
    <li class="continued">Management Access</li>
    <li><svg><use href="#tick"/></svg>Access to our Internal Brokerage Forum</li>
    <li><svg><use href="#tick"/></svg>Company Profit Sharing!</li>
    <li><svg><use href="#tick"/></svg>Private Offices Available to Rent</li>
  </ul>

  <section class="perks">
    <div class="notch-perks"></div>
    <div class="perk perk-1">
      <svg viewBox="0 0 76 76" fill="none" stroke="#fff" stroke-width="2.5">
        <path d="M14 30l12-14h24l12 14-24 30z"/>
        <circle cx="42" cy="42" r="11"/>
        <path d="M50 50l10 10"/>
      </svg>
      Lead Generation<br>Software with over<br>3,000 Leads
    </div>
    <div class="divider" style="left:249px"></div>
    <div class="perk perk-2">
      <svg viewBox="0 0 76 76" fill="none" stroke="#fff" stroke-width="2.5">
        <path d="M38 6c10 10 12 24 10 40H28C26 30 28 16 38 6z"/>
        <path d="M28 38l-10 14h12M48 38l10 14H46"/>
        <path d="M34 56v10M42 56v10"/>
      </svg>
      10 Leads to<br>Start
    </div>
    <div class="divider" style="left:459px"></div>
    <div class="perk perk-3">
      <svg viewBox="0 0 76 76" fill="none" stroke="#fff" stroke-width="2.5">
        <rect x="10" y="10" width="56" height="56"/>
        <path d="M10 20h56"/>
        <text x="38" y="60" text-anchor="middle" fill="#fff" stroke="none" font-family="Josefin Sans, sans-serif" font-size="15">CRM</text>
      </svg>
      Free Personal CRM<br>and Website
    </div>
    <div class="divider" style="left:707px"></div>
    <div class="perk perk-4">
      <svg viewBox="0 0 76 76" fill="none" stroke="#fff" stroke-width="2.5">
        <circle cx="38" cy="32" r="18"/>
        <circle cx="16" cy="14" r="7"/>
        <circle cx="62" cy="50" r="7"/>
        <rect x="28" y="56" width="20" height="14"/>
      </svg>
      Restrictions and<br>Rules apply
    </div>
  </section>

  <footer class="contact"></footer>
  <div class="address-tab">
    <svg viewBox="0 0 215 44" width="215" height="44"><polygon points="18,0 197,0 215,22 197,44 18,44 0,22" fill="#fff"/></svg>
    <span>Address</span>
  </div>
  <div class="contact-line">
    <span class="contact-item">
      <svg viewBox="0 0 16 20"><path d="M8 0a7 7 0 0 0-7 7c0 5 7 13 7 13s7-8 7-13a7 7 0 0 0-7-7zm0 10a3 3 0 1 1 0-6 3 3 0 0 1 0 6z" fill="#273b7b"/></svg>
      4817 Marlow Creek Road, Suite 412, Fairfax, VA 22147
    </span>
    <span class="sep">|</span>
    <span class="contact-item contact-phone">
      <svg viewBox="0 0 20 20" style="width:19px;height:19px"><path d="M4 1l4 4-2 3c1 3 3 5 6 6l3-2 4 4-3 3C8 19 1 12 1 4z" fill="none" stroke="#273b7b" stroke-width="2"/></svg>
      703-241-7086
    </span>
    <span class="sep">|</span>
    <span class="contact-item">
      <svg viewBox="0 0 20 14" style="width:19px;height:13px"><rect width="20" height="14" fill="#273b7b"/><path d="M1 1l9 7 9-7" fill="none" stroke="#d6d7d9" stroke-width="1.5"/></svg>
      info@veltrahomes.example
    </span>
  </div>

</div>
</body>
</html>
```